Sell the dream! Property investment proposal document

We are looking for a proposal document which outlines our vision for property development. The purpose of the document is to raise investment from investors - sell the dream!
Brief summary:
Tarrow Dwellings Developments, is an emerging New Zealand property investment company with a focus on providing unique property investment opportunities.
Our expertise and capabilities in architectural modular homes provide us with a remarkable advantage in tackling the development of properties that are typically considered challenging, remote, or uniquely positioned.
Our specialization in this niche sector of property development not only sets us apart from competitors, but also paves the way for lucrative investment opportunities in the New Zealand property market.
Feel free to use any images from www.tarrowdwellings.co.nz
Target Market(s)
investors for a unique property development opportunity
Industry/Entity Type
luxury property development in unique locations throughout New Zealand
Font styles to use
Colors
Designer to choose only greyscale colors for use in the design.
Look and feel

```html
<!DOCTYPE html>
<html lang="en">
<head>
<meta charset="utf-8">
<title>Tarrow Dwellings Developments – Business Overview</title>
<link rel="stylesheet" href="https://fonts.googleapis.com/css2?family=Poppins:wght@300;400;500;600&display=swap">
<style>
:root{
  --sheet:#b3b3b3;
  --page:#161616;
  --pattern:#1f1f1f;
  --ink:#ffffff;
  --ink-soft:#d2d2d2;
  --ink-muted:#a8a8a8;
  --ink-dark:#1b1b1b;
}
*{margin:0;padding:0;box-sizing:border-box}
html,body{width:775px;height:1200px;overflow:hidden;background:var(--sheet)}
body{position:relative;font-family:"Poppins",sans-serif;color:var(--ink)}
.spread{position:absolute;left:63px;width:648px;height:229px;background:var(--page);overflow:hidden;box-shadow:3px 4px 6px rgba(0,0,0,.28)}
.spread > *{position:absolute}
.photo{display:block}
.pattern-band{background:var(--pattern)}
.url{font-size:4.4px;letter-spacing:2.2px;color:var(--ink-soft);top:205px}
.page-no{font-size:4.4px;letter-spacing:2.2px;color:var(--ink-soft);top:205px}
.body-copy{font-size:3.6px;line-height:1.45;font-weight:300;color:var(--ink-soft)}
.body-copy p + p{margin-top:4px}
.section-title{font-size:9px;font-weight:300;letter-spacing:.1px;line-height:1}
.section-title b{font-weight:500}
/* cover */
.brand-name{font-size:19px;font-weight:400;letter-spacing:-.3px;line-height:1}
.cover-title{font-size:22px;font-weight:600;line-height:1;letter-spacing:.2px}
.cover-sub{font-size:8.5px;font-weight:300;letter-spacing:4.6px;line-height:1}
.contact{font-size:4.6px;letter-spacing:.9px;color:var(--ink-soft);text-align:right;line-height:1.75}
.contact svg{width:4px;height:4px;vertical-align:-0.5px;margin-right:1.5px}
.lead{font-size:7px;font-weight:300;line-height:1.18}
.callout{font-size:8px;font-weight:300;line-height:1.18;text-transform:uppercase}
.callout-sub{font-size:4.8px;font-weight:300;line-height:1.3;color:var(--ink-soft)}
.origins-copy{font-size:5px;line-height:1.3;font-weight:400;color:var(--ink-dark)}
</style>
</head>
<body>

<!-- Cover spread -->
<section class="spread" style="top:67px">
  <div class="pattern-band" style="left:0;top:0;width:49px;height:229px" role="img" aria-label="Faint geometric diamond pattern strip"></div>
  <div class="photo" style="left:151px;top:95px;width:50px;height:38px;background:linear-gradient(160deg,#3d4a33,#1e231b)" role="img" aria-label="Dusk view of a modular home beside a pool"></div>
  <div class="photo" style="left:202px;top:95px;width:53px;height:38px;background:linear-gradient(180deg,#2a2a2a,#111)" role="img" aria-label="Dark timber kitchen interior"></div>
  <div class="photo" style="left:256px;top:95px;width:40px;height:38px;background:linear-gradient(180deg,#c9c9bd,#6b6a45 70%,#4d4a2c)" role="img" aria-label="Countryside view through a window with trees"></div>
  <div class="contact" style="right:352px;top:140px">
    <div><svg viewBox="0 0 10 10"><path d="M2 1l2 2-1 1.3c.6 1.2 1.5 2.1 2.7 2.7L7 6l2 2-1.2 1.2C4.5 9 1 5.5.8 2.2z" fill="none" stroke="#d2d2d2" stroke-width=".9"/></svg>09 555 0142</div>
    <div><svg viewBox="0 0 10 10"><rect x="1" y="2" width="8" height="6" fill="none" stroke="#d2d2d2" stroke-width=".9"/><path d="M1 2l4 3.2L9 2" fill="none" stroke="#d2d2d2" stroke-width=".9"/></svg>SALES@TARROWDWELLINGS.CO.NZ</div>
  </div>
  <div class="url" style="left:199px;width:97px;text-align:right;letter-spacing:1.6px">WWW.TARROWDWELLINGS.CO.NZ</div>
  <div class="brand-name" style="left:349px;top:21px">Tarrow</div>
  <div class="cover-title" style="left:349px;top:141px">BUSINESS</div>
  <div class="cover-sub" style="left:350px;top:164px">OVERVIEW</div>
  <div class="url" style="left:350px;letter-spacing:1.6px">WWW.TARROWDWELLINGS.CO.NZ</div>
  <div class="photo" style="left:485px;top:0;width:163px;height:229px;background:linear-gradient(180deg,#4a4236 0%,#a9a79a 25%,#8b8a6e 50%,#5b5648 75%,#2e2c28 100%)" role="img" aria-label="Glass-walled living room with a lounge chair overlooking mountains"></div>
</section>

<!-- Pages 1–2 -->
<section class="spread" style="top:348px">
  <div class="pattern-band" style="left:24px;top:0;width:135px;height:34px" role="img" aria-label="Faint geometric diamond pattern band"></div>
  <div class="photo" style="left:24px;top:37px;width:135px;height:136px;background:linear-gradient(180deg,#8a8373 0%,#b9a88a 25%,#6a6240 45%,#4f4a25 75%,#3a3518 100%)" role="img" aria-label="Modular home on coastal farmland at sunset with a winding driveway"></div>
  <div class="lead" style="left:193px;top:36px;width:108px">Tarrow Dwellings Developments, is an emerging New Zealand property investment company with a focus on providing unique property investment opportunities.</div>
  <div class="body-copy" style="left:193px;top:97px;width:102px">
    <p>Our expertise and capabilities in architectural modular homes provide us with a remarkable advantage in tackling the development of properties that are typically considered challenging, remote, or uniquely positioned.</p>
    <p>As a company, with 48 employees boasting a wealth of experience in handling complex architectural projects, making us well-equipped to navigate the intricacies and demands of such ventures.</p>
  </div>
  <div class="url" style="left:24px">WWW.TARROWDWELLINGS.CO.NZ</div>
  <div class="page-no" style="left:285px">PG 1</div>

  <div class="photo" style="left:348px;top:37px;width:123px;height:53px;background:linear-gradient(180deg,#c9d3da 0%,#6a7683 35%,#5f7045 55%,#8c8a7a 80%,#3a3530 100%)" role="img" aria-label="Open living space with pebble seats looking over green hills and harbour"></div>
  <div class="photo" style="left:473px;top:37px;width:123px;height:53px;background:linear-gradient(180deg,#d8dee3 0%,#7fa5c3 40%,#5d88ad 60%,#2c2a28 85%,#1a1918 100%)" role="img" aria-label="Lounge chairs in a glazed room facing the ocean"></div>
  <div class="callout" style="left:347px;top:111px;width:100px">This advantage allows us to not only execute projects efficiently</div>
  <div class="callout-sub" style="left:347px;top:153px;width:100px">but also to deliver exceptional results within condensed time frames.</div>
  <div class="body-copy" style="left:473px;top:109px;width:116px">
    <p>By capitalizing on our ability to develop difficult, remote, or one-of-a-kind properties swiftly and effectively, Tarrow Dwellings Developments offers investors a rare chance to engage in projects that promise exceptional profitability in the New Zealand property market.</p>
    <p>Our specialization in this niche sector of property development not only sets us apart from competitors, but also paves the way for lucrative investment opportunities in the New Zealand property market</p>
  </div>
  <div class="pattern-band" style="left:598px;top:0;width:50px;height:229px" role="img" aria-label="Faint geometric diamond pattern strip"></div>
  <div class="url" style="left:347px">WWW.TARROWDWELLINGS.CO.NZ</div>
  <div class="page-no" style="left:608px">PG 2</div>
</section>

<!-- Pages 3–4 -->
<section class="spread" style="top:630px">
  <div class="photo" style="left:0;top:0;width:159px;height:229px;background:linear-gradient(180deg,#f7f8fc 0%,#e6ebf6 40%,#9a9a98 55%,#3b3b3b 65%,#5f6e3c 78%,#6d8a3a 90%,#4c5e2a 100%)" role="img" aria-label="Cantilevered dark-clad home above rocks and green grass against a pale sky"></div>
  <div class="section-title" style="left:22px;top:25px;color:var(--ink-dark)"><b>BUSINESS</b> ORIGINS</div>
  <div class="origins-copy" style="left:23px;top:40px;width:106px">Tarrow Dwellings Developments was established with the goal of transforming the property investment market in New Zealand by introducing an innovative approach that centers on architectural modular designs and streamlined project timelines.</div>
  <div class="url" style="left:24px">WWW.TARROWDWELLINGS.CO.NZ</div>
  <div class="pattern-band" style="left:196px;top:0;width:104px;height:31px" role="img" aria-label="Faint geometric diamond pattern band"></div>
  <div class="body-copy" style="left:196px;top:40px;width:104px">
    <p>Driven by our enthusiasm for architecture and real estate, we have expanded our successful business model to not only offer financial opportunities for investors but also to expand on our passion for high-end architectural design.</p>
    <p>With a wealth of experience accumulated over the past six years in the construction and the property market, we are pivoting to focus solely on our property development initiatives, presenting completed Tarrow projects to the market, in exclusive locations.</p>
    <p>These projects will boast high-quality standards, meticulous attention to detail and landscaping, and creative design elements. By introducing completed Tarrow properties into the market, we aim to reach a wider audience, catering to individuals who prefer ready-to-occupy homes, over engaging in the design and construction process. This approach also simplifies the financing process for prospective buyers, as established properties are often preferred by financial lenders.</p>
  </div>
  <div class="page-no" style="left:284px">PG 3</div>

  <div class="section-title" style="left:347px;top:25px"><b>COMPETITIVE</b> ADVANTAGE</div>
  <div class="photo" style="left:348px;top:41px;width:115px;height:130px;background:linear-gradient(180deg,#7d8794 0%,#c8bfae 30%,#d9c7a0 45%,#6b6a66 60%,#55514b 80%,#3d3a36 100%)" role="img" aria-label="Glass pavilion home on a pebble shore at sunset"></div>
  <div class="body-copy" style="left:481px;top:40px;width:108px">
    <p>Our competitive advantage lies in the uniqueness of our property investment opportunities.</p>
    <p>Unlike traditional real estate companies, we focus on offering properties that are not only profitable but also aesthetically pleasing and unique. By catering to the tastes of architecture lovers, we set ourselves apart from the competition and attract a niche market of customers who appreciate the artistry and design of our projects.</p>
  </div>
  <div class="lead" style="left:481px;top:101px;width:100px">Additionally, the streamlined and condensed timelines facilitated by our modular approach provide quicker returns on investment.</div>
  <div class="pattern-band" style="left:598px;top:0;width:50px;height:229px" role="img" aria-label="Faint geometric diamond pattern strip"></div>
  <div class="url" style="left:347px">WWW.TARROWDWELLINGS.CO.NZ</div>
  <div class="page-no" style="left:608px">PG 4</div>
</section>

<!-- Pages 5–6 -->
<section class="spread" style="top:908px">
  <div class="section-title" style="left:24px;top:25px"><b>FINANCIAL</b> SUMMARY</div>
  <div class="photo" style="left:25px;top:42px;width:141px;height:149px;background:linear-gradient(180deg,#dcd9d2 0%,#b8c6d6 20%,#6e7f92 38%,#4f6a36 52%,#7c8f58 65%,#c8b9a0 82%,#8a7a66 100%)" role="img" aria-label="Floor-to-ceiling window framing hills and harbour, with pebble seats on timber floor"></div>
  <div class="pattern-band" style="left:196px;top:0;width:104px;height:107px" role="img" aria-label="Faint geometric diamond pattern block"></div>
  <div class="body-copy" style="left:196px;top:118px;width:104px">
    <p>In terms of financial projections, with each development, we anticipate a profit of 10%-20% which will be project dependent.</p>
    <p>This growth is fueled by the increasing demand for unique property investments in New Zealand and our ability to deliver high-quality services to the market in a condensed time frame, with heavily controlled costs.</p>
    <p>With a solid business model and a dedicated team, we are confident in our ability to achieve success and establish Tarrow Dwellings Investments as a trusted name in the industry</p>
  </div>
  <div class="url" style="left:24px">WWW.TARROWDWELLINGS.CO.NZ</div>
  <div class="page-no" style="left:284px">PG 5</div>

  <div class="body-copy" style="left:346px;top:27px;width:238px">New Zealand's property market has been experiencing steady growth over the years, making it an attractive destination for property investors. With its beautiful landscapes and strong economy, New Zealand offers a diverse range of investment opportunities for both local and international investors. The demand for quality properties in prime locations continues to rise, creating a favorable environment for property investment companies like ours that can lean on our modular benefits of being able to reach unique and remote locations</div>
  <div class="photo" style="left:346px;top:71px;width:75px;height:82px;background:linear-gradient(180deg,#9c968d 0%,#cfd2d3 35%,#b7b2aa 60%,#d9d6d0 100%)" role="img" aria-label="Bedroom with linen bed beside a window view"></div>
  <div class="photo" style="left:425px;top:71px;width:75px;height:82px;background:linear-gradient(90deg,#a89f93 0%,#6a6560 40%,#4a4a4a 70%,#2f2f2f 100%)" role="img" aria-label="Bathroom with towel rail and dark stone wall"></div>
  <div class="photo" style="left:505px;top:71px;width:75px;height:82px;background:linear-gradient(180deg,#e4e7ea 0%,#c9cfd4 35%,#5b5c5a 55%,#7b7a4e 75%,#9a8f6c 100%)" role="img" aria-label="Low modular homes among coastal grasses and a tree"></div>
  <div class="pattern-band" style="left:598px;top:0;width:50px;height:229px" role="img" aria-label="Faint geometric diamond pattern strip"></div>
  <div class="url" style="left:347px">WWW.TARROWDWELLINGS.CO.NZ</div>
  <div class="page-no" style="left:608px">PG 6</div>
</section>

</body>
</html>
```